Flyer for Mountain Bike Skills Event

Create an 11x17 posts for an upcoming Mountain Bike Skills event.

Falcon Trail Riding Academy Logo
--
Are you ready to ride your mountain bike faster and with more confidence? Join us to learn how to take your riding to the next level!
--
EVENT INFORMATION:

Saturday April 23
>> Fundamental Skills Clinic
>> Jumping Mini Clinic

Sunday April 24
>> Intermediate / Advanced Skills Clinic

Saturday - Sunday April 23/24
>> 2 Day Skills Camp

--
San Diego, California
--
Following your clinic, you will see an immediate improvement in your riding and a boost in confidence.

Skills taught and practiced in courses include:

Mind skills
Mastering manual front-wheel lifts
Manual dropping roots & steps
Cornering with speed & confidence
Reading & breaking down the trail
Introduction to energy management & flow
Linking trail sections for flow
Attacking flat corners
Flat and cambered corners
Bermed corners; lines and pumping
Switchbacks
Maximizing grip and traction with pumping
Learning to pump for speed & air

Event hosted by: HARLOWE CYCLE DEPOT (*use logo)

Sign up today!
--
More informaiton on our website:
WWW.PEDALWITHPOISE.COM

Target Market(s)

Mountain bikers age 35-60

Industry/Entity Type

Fitness

Requirements
Must have
• Falcon Logo
• Should be consistent with the Falcon brand, see website for examples: https://coastaltrailcraftlessons.com/ and our truck wrap design file.
• Flyer needs to be easy to read and include all the content in the project description.
Nice to have
• Include our tag line: SOAR LIKE A FALCON

```html
<!DOCTYPE html>
<html lang="en">
<head>
<meta charset="utf-8">
<title>Falcon Trail Riding Academy – Skills Clinic Flyer</title>
<link rel="stylesheet" href="https://fonts.googleapis.com/css2?family=Exo+2:ital,wght@0,700;0,800;1,700;1,800&family=Roboto:wght@400;500;700&family=Varela+Round&display=swap">
<style>
  :root {
    --ink: #1b1a1c;
    --night: #0d0d0e;
    --pink: #e8185a;
    --sky: #8fd3ee;
    --slate: #6f6f73;
    --paper: #ffffff;
    --mist: #d7eaf6;
  }
  * { box-sizing: border-box; margin: 0; padding: 0; }
  html, body { width: 1200px; height: 848px; overflow: hidden; background: var(--paper); }
  .flyer {
    position: relative; width: 1200px; height: 848px; overflow: hidden;
    background: linear-gradient(180deg, var(--mist) 0%, #f4f9fc 45%, var(--paper) 60%);
    font-family: "Roboto", Arial, sans-serif; color: var(--ink);
  }
  .backdrop { position: absolute; inset: 0; }
  .rider-photo {
    position: absolute; left: 510px; top: 60px; width: 390px; height: 788px;
    background: linear-gradient(180deg, #a9cde6 0%, #c9dcea 28%, #b89a7a 55%, #7a5a3e 75%, #2a2420 100%);
    opacity: .85;
    clip-path: polygon(15% 0, 88% 2%, 100% 40%, 92% 100%, 4% 100%, 0 45%);
  }
  /* logo */
  .brand { position: absolute; left: 62px; top: 66px; display: flex; align-items: center; gap: 16px; }
  .brand-name { font-family: "Exo 2", sans-serif; font-weight: 800; font-size: 34px; line-height: 1.02; color: var(--ink); text-transform: uppercase; }
  .brand-dot { width: 58px; height: 58px; border-radius: 50%; background: var(--pink); }
  /* headline */
  .headline { position: absolute; left: 0; top: 262px; font-family: "Exo 2", sans-serif; font-style: italic; font-weight: 800; text-transform: uppercase; }
  .band { position: absolute; left: 0; display: flex; align-items: center; white-space: nowrap; }
  .band-ask { top: 0; width: 660px; height: 42px; padding-left: 100px; font-size: 31px; color: var(--paper); background: rgba(80,80,84,.9); clip-path: polygon(0 0, 100% 0, 97% 100%, 0 100%); }
  .band-bike { top: 52px; width: 670px; height: 80px; padding-left: 98px; font-size: 64px; color: var(--ink); background: var(--paper); clip-path: polygon(0 0, 100% 0, 97% 100%, 0 100%); }
  .band-pace { top: 142px; width: 680px; height: 40px; padding-left: 100px; font-size: 28px; color: var(--paper); background: rgba(45,45,48,.9); clip-path: polygon(0 0, 100% 0, 97% 100%, 0 100%); }
  .accent { color: var(--sky); }
  /* schedule */
  .schedule { position: absolute; left: 94px; top: 545px; width: 190px; }
  .day { margin-bottom: 22px; }
  .day-date { font-weight: 700; font-size: 16px; color: var(--sky); margin-bottom: 14px; }
  .day-event { font-weight: 700; font-size: 13.5px; color: var(--paper); line-height: 1.35; }
  .venue {
    position: absolute; left: 310px; top: 606px; width: 100px; height: 100px;
    border: 3px solid var(--paper); border-radius: 14px; background: var(--night);
    display: flex; flex-direction: column; justify-content: center; align-items: center; text-align: center;
  }
  .venue-label { font-weight: 700; font-size: 13px; color: var(--pink); }
  .venue-place { font-weight: 700; font-size: 13px; color: var(--paper); line-height: 1.2; margin-top: 2px; }
  .host { position: absolute; left: 300px; top: 716px; width: 120px; text-align: center; color: var(--paper); }
  .host-badge { width: 52px; height: 52px; border-radius: 50%; background: var(--paper); margin: 0 auto 6px; }
  .host-label { font-size: 8.5px; line-height: 1.25; }
  .host-name { font-size: 9px; font-weight: 700; }
  .signup { position: absolute; left: 420px; top: 612px; width: 180px; height: 180px; }
  .signup-text {
    position: absolute; inset: 0; display: flex; flex-direction: column; justify-content: center; align-items: center;
    font-family: "Varela Round", sans-serif; color: var(--paper); transform: rotate(-12deg); line-height: 1;
  }
  .signup-text .line-1 { font-size: 29px; }
  .signup-text .line-2 { font-size: 37px; }
  /* right column */
  .promise { position: absolute; right: 72px; top: 72px; width: 420px; text-align: right; font-size: 20px; font-weight: 500; line-height: 1.3; color: var(--ink); }
  .skills-title { position: absolute; right: 72px; top: 182px; text-align: right; font-size: 28px; font-weight: 500; line-height: 1.15; color: var(--pink); }
  .skills { position: absolute; right: 72px; top: 276px; list-style: none; text-align: right; }
  .skills li { font-size: 15.5px; line-height: 22.5px; color: var(--ink); display: flex; justify-content: flex-end; align-items: center; gap: 7px; }
  .skills li::after { content: ""; width: 7px; height: 7px; border-top: 2.5px solid var(--pink); border-right: 2.5px solid var(--pink); transform: rotate(45deg); margin-right: 4px; }
  .tagline { position: absolute; right: 0; top: 636px; width: 600px; height: 60px; background: rgba(30,30,32,.92);
    clip-path: polygon(3% 0, 100% 0, 100% 100%, 0 100%);
    display: flex; align-items: center; padding-left: 38px;
    font-family: "Exo 2", sans-serif; font-style: italic; font-weight: 800; font-size: 38px; color: var(--paper); text-transform: uppercase; white-space: nowrap; }
  .subline { position: absolute; right: 72px; top: 704px; font-family: "Exo 2", sans-serif; font-style: italic; font-weight: 800; font-size: 18px; color: var(--paper); text-transform: uppercase; }
  .website { position: absolute; right: 72px; top: 752px; text-align: right; }
  .website-lead { font-size: 22px; font-weight: 500; color: var(--paper); }
  .website-url { font-size: 26px; font-weight: 700; color: var(--pink); letter-spacing: .5px; margin-top: 4px; }
</style>
</head>
<body>
<main class="flyer">
  <svg class="backdrop" width="1200" height="848" viewBox="0 0 1200 848" aria-hidden="true">
    <polygon points="0,470 1200,628 1200,848 0,848" fill="#0d0d0e"/>
    <polygon points="0,445 560,470 640,530 0,500" fill="#e8185a"/>
    <polygon points="0,512 520,535 600,580 0,545" fill="#e8185a"/>
    <polygon points="640,610 1200,640 1200,660 700,640" fill="#e8185a"/>
  </svg>

  <div class="rider-photo" role="img" aria-label="Photo of a mountain biker in helmet and goggles descending a rocky dirt trail"></div>

  <div class="brand">
    <div class="brand-name">Falcon Trail<br>Riding Academy</div>
    <div class="brand-dot" aria-hidden="true"></div>
  </div>

  <h1 class="headline">
    <span class="band band-ask">Are you&nbsp;<span class="accent">ready to ride</span>&nbsp;your</span>
    <span class="band band-bike">Mountain Bike</span>
    <span class="band band-pace"><span class="accent">Faster</span>&nbsp;and with more&nbsp;<span class="accent">confidence?</span></span>
  </h1>

  <section class="schedule">
    <div class="day">
      <p class="day-date">Saturday April 23</p>
      <p class="day-event">Fundamental Skills Clinic<br>Jumping Mini Clinic</p>
    </div>
    <div class="day">
      <p class="day-date">Sunday April 24</p>
      <p class="day-event">Intermediate / Advanced<br>Skills Clinic</p>
    </div>
    <div class="day">
      <p class="day-date">Saturday - Sunday<br>April 23/24</p>
      <p class="day-event">2 Day Skills Camp</p>
    </div>
  </section>

  <div class="venue">
    <span class="venue-label">VENUE</span>
    <span class="venue-place">SAN DIEGO,<br>CALIFORNIA</span>
  </div>

  <div class="host">
    <div class="host-badge" aria-hidden="true"></div>
    <p class="host-label">Event hosted by</p>
    <p class="host-name">HARLOWE CYCLE DEPOT</p>
  </div>

  <div class="signup">
    <svg width="180" height="180" viewBox="0 0 180 180" aria-hidden="true">
      <polygon fill="rgba(120,120,124,.9)" stroke="#fff" stroke-width="4"
        points="90,6 102,28 124,14 127,39 153,36 144,60 168,70 149,87 166,106 141,113 148,139 122,136 117,162 96,148 82,170 72,146 48,158 48,132 22,130 34,107 10,94 31,80 16,58 42,54 40,28 64,36 72,12"/>
    </svg>
    <div class="signup-text"><span class="line-1">Sign Up</span><span class="line-2">NOW!</span></div>
  </div>

  <p class="promise">Following your clinic, you will see an immediate improvement in your riding and a boost in confidence.</p>

  <h2 class="skills-title">Skills taught and practiced<br>in courses include:</h2>
  <ul class="skills">
    <li>Mind skills</li>
    <li>Mastering manual front-wheel lifts</li>
    <li>Manual dropping roots &amp; steps</li>
    <li>Cornering with speed and confidence</li>
    <li>Reading &amp; breaking down the trail</li>
    <li>Introduction to energy management &amp; flow</li>
    <li>Linking trail sections for flow</li>
    <li>Attacking flat corners</li>
    <li>Flat and cambered corners</li>
    <li>Bermed corners; lines and pumping</li>
    <li>Switchbacks</li>
    <li>Maximizing grip and traction with pumping</li>
    <li>Learning to pump for speed &amp; air</li>
  </ul>

  <p class="tagline">Soar like a&nbsp;<span class="accent">Falcon</span></p>
  <p class="subline">Take your riding to the <span class="accent">next level</span></p>

  <div class="website">
    <p class="website-lead">More information on our website:</p>
    <p class="website-url">WWW.PEDALWITHPOISE.COM</p>
  </div>
</main>
</body>
</html>
```